Graphical circular representation of our 4-step process

We need a graphic to use on a printed sales sheet, enlarged to use on back wall of our Trade Show booth, and on our website that shows our 4-step process. We are an Air and Surface Purification company and want a piece that will convey what we do easily to potential clients. We see it as a circular process that repeats. We are happy with the descriptive wording (although open to other ideas) but need help with producing final layout and artwork.
Please see the attached photo of what we have developed so far.
Photo/graphic for "Quantify" is a Barnaby Quillfeather type magnifying lens showing a host of bacterial pathogens. Photo/graphic for "Decontaminate" shows same image of bacterial pathogens but with 90% of them missing. Not sure what the photo/graphic should be under "Prevent". Photo/graphic under "Maintain" would be a computer monitor and cell phone showing the display of the App we have for clients to monitor their facilities.

Target Market(s)

Commercial Food production facilities

Font styles to use
Sans Serif

Colors

Designer to choose colors to be used in the design.

Requirements
Must have
• Crisp, Clean and Professional. We will use on web, on 8.5" x 11" Gloss Sales Sheet and enlarge to fit on a 7" x 7" trade show booth background wall
Nice to have
• Our target clients are food safety professionals concerned with the purity of their foods and finished products.

```html
<!DOCTYPE html>
<html lang="en">
<head>
<meta charset="utf-8">
<title>4-Step Protection Cycle</title>
<link rel="stylesheet" href="https://fonts.googleapis.com/css2?family=Oswald:wght@500;700&family=Saira+Semi+Condensed:wght@600&display=swap">
<style>
  :root {
    --page-bg: #ececec;
    --disk: #f7f7f7;
    --divider: #e2e2e2;
    --ink: #111111;
    --green: #2fd35a;
    --teal: #2cbba0;
    --blue: #3ba8d8;
    --dots: #1f4470;
    --label: #ffffff;
  }
  html, body {
    margin: 0;
    padding: 0;
    width: 1200px;
    height: 860px;
    overflow: hidden;
    background: var(--page-bg);
  }
  .cycle-graphic {
    display: block;
    width: 1200px;
    height: 860px;
    background: radial-gradient(circle at 50% 50%, #f8f8f8 0%, var(--page-bg) 70%);
  }
  .stage-label {
    font-family: "Oswald", sans-serif;
    font-weight: 500;
    font-size: 27px;
    letter-spacing: 1px;
    fill: var(--label);
  }
  .step-text {
    font-family: "Saira Semi Condensed", sans-serif;
    font-weight: 600;
    font-size: 24px;
    fill: var(--ink);
  }
  .hub-number {
    font-family: "Oswald", sans-serif;
    font-weight: 700;
    font-size: 100px;
    fill: var(--ink);
  }
  .hub-word {
    font-family: "Oswald", sans-serif;
    font-weight: 500;
    font-size: 40px;
    fill: var(--ink);
  }
  .cycle-dots {
    fill: none;
    stroke: var(--dots);
    stroke-width: 6;
    stroke-linecap: round;
    stroke-dasharray: 0 13;
  }
  .step-divider { stroke: #cfcfcf; stroke-width: 1.5; }
</style>
</head>
<body>
<svg class="cycle-graphic" viewBox="0 0 1200 860" xmlns="http://www.w3.org/2000/svg">
  <defs>
    <linearGradient id="band-top" x1="375" y1="0" x2="825" y2="0" gradientUnits="userSpaceOnUse">
      <stop offset="0" stop-color="var(--blue)"/><stop offset="0.5" stop-color="var(--teal)"/><stop offset="1" stop-color="var(--green)"/>
    </linearGradient>
    <linearGradient id="band-right" x1="0" y1="205" x2="0" y2="655" gradientUnits="userSpaceOnUse">
      <stop offset="0" stop-color="var(--blue)"/><stop offset="0.5" stop-color="var(--teal)"/><stop offset="1" stop-color="var(--green)"/>
    </linearGradient>
    <linearGradient id="band-bottom" x1="825" y1="0" x2="375" y2="0" gradientUnits="userSpaceOnUse">
      <stop offset="0" stop-color="var(--blue)"/><stop offset="0.5" stop-color="var(--teal)"/><stop offset="1" stop-color="var(--green)"/>
    </linearGradient>
    <linearGradient id="band-left" x1="0" y1="655" x2="0" y2="205" gradientUnits="userSpaceOnUse">
      <stop offset="0" stop-color="var(--blue)"/><stop offset="0.5" stop-color="var(--teal)"/><stop offset="1" stop-color="var(--green)"/>
    </linearGradient>
    <radialGradient id="disk-fill" cx="50%" cy="50%" r="50%">
      <stop offset="0" stop-color="#ffffff"/><stop offset="1" stop-color="var(--disk)"/>
    </radialGradient>
    <radialGradient id="lens-fill" cx="45%" cy="40%" r="60%">
      <stop offset="0" stop-color="#f4f6f5"/><stop offset="0.6" stop-color="#b9d9cf"/><stop offset="1" stop-color="#7f8f96"/>
    </radialGradient>
    <linearGradient id="shield-fill" x1="0" y1="0" x2="1" y2="1">
      <stop offset="0" stop-color="#e8403c"/><stop offset="1" stop-color="#a40f12"/>
    </linearGradient>
    <linearGradient id="device-fill" x1="0" y1="0" x2="0" y2="1">
      <stop offset="0" stop-color="#2a2f3a"/><stop offset="1" stop-color="#c9ccd2"/>
    </linearGradient>
    <filter id="soft-shadow" x="-20%" y="-20%" width="140%" height="140%">
      <feDropShadow dx="0" dy="6" stdDeviation="8" flood-color="#000" flood-opacity="0.18"/>
    </filter>
    <marker id="dot-arrow" viewBox="0 0 10 10" refX="5" refY="5" markerWidth="5" markerHeight="5" orient="auto" markerUnits="strokeWidth">
      <path d="M0,0 L10,5 L0,10 z" fill="var(--dots)"/>
    </marker>

    <path id="label-top" d="M375.2,142.4 A365,365 0 0 1 824.8,142.4"/>
    <path id="label-right" d="M887.6,205.2 A365,365 0 0 1 887.6,654.8"/>
    <path id="label-bottom" d="M375.2,717.6 A365,365 0 0 0 824.8,717.6"/>
    <path id="label-left" d="M312.4,654.8 A365,365 0 0 1 312.4,205.2"/>
  </defs>

  <!-- dotted cycle arrows -->
  <g class="cycle-arrows">
    <path class="cycle-dots" d="M332.4,132.8 A400,400 0 0 1 867.6,132.8" marker-end="url(#dot-arrow)"/>
    <path class="cycle-dots" d="M897.2,162.4 A400,400 0 0 1 897.2,697.6" marker-end="url(#dot-arrow)"/>
    <path class="cycle-dots" d="M867.6,727.2 A400,400 0 0 1 332.4,727.2" marker-end="url(#dot-arrow)"/>
    <path class="cycle-dots" d="M302.8,697.6 A400,400 0 0 1 302.8,162.4" marker-end="url(#dot-arrow)"/>
  </g>

  <!-- inner disk with quadrant dividers -->
  <circle cx="600" cy="430" r="340" fill="url(#disk-fill)" filter="url(#soft-shadow)"/>
  <g class="quadrant-dividers" stroke="var(--divider)" stroke-width="34">
    <line x1="360" y1="190" x2="840" y2="670"/>
    <line x1="840" y1="190" x2="360" y2="670"/>
  </g>

  <!-- stage bands -->
  <g class="stage-bands" fill="none" stroke-width="40" stroke-linecap="round">
    <use href="#label-top" stroke="url(#band-top)"/>
    <use href="#label-right" stroke="url(#band-right)"/>
    <use href="#label-bottom" stroke="url(#band-bottom)"/>
    <use href="#label-left" stroke="url(#band-left)"/>
  </g>
  <g class="stage-labels">
    <text class="stage-label" dominant-baseline="central"><textPath href="#label-top" startOffset="50%" text-anchor="middle">QUANTIFY</textPath></text>
    <text class="stage-label" dominant-baseline="central"><textPath href="#label-right" startOffset="50%" text-anchor="middle">DECONTAMINATE</textPath></text>
    <text class="stage-label" dominant-baseline="central"><textPath href="#label-bottom" startOffset="50%" text-anchor="middle">PREVENT</textPath></text>
    <text class="stage-label" dominant-baseline="central"><textPath href="#label-left" startOffset="50%" text-anchor="middle">MAINTAIN</textPath></text>
  </g>

  <!-- central hub -->
  <circle cx="600" cy="430" r="135" fill="#ffffff" filter="url(#soft-shadow)"/>
  <text class="hub-number" x="600" y="432" text-anchor="middle">24/7</text>
  <text class="hub-word" x="600" y="482" text-anchor="middle">PROTECTION</text>

  <!-- quantify step -->
  <g class="step step-quantify">
    <circle cx="524" cy="200" r="58" fill="url(#lens-fill)" role="img" aria-label="Magnifying lens over a mix of bacterial pathogens"/>
    <line class="step-divider" x1="612" y1="150" x2="612" y2="228"/>
    <text class="step-text" x="634" y="153">Determine</text>
    <text class="step-text" x="634" y="184">microbial</text>
    <text class="step-text" x="634" y="215">levels</text>
  </g>

  <!-- decontaminate step -->
  <g class="step step-decontaminate">
    <circle cx="833" cy="385" r="60" fill="url(#lens-fill)" role="img" aria-label="Lens showing bacterial pathogens crossed out and reduced"/>
    <text class="step-text" x="792" y="479">Reduce</text>
    <text class="step-text" x="792" y="510">microbial</text>
    <text class="step-text" x="792" y="541">levels</text>
  </g>

  <!-- prevent step -->
  <g class="step step-prevent">
    <rect x="480" y="600" width="104" height="136" rx="18" fill="url(#shield-fill)" role="img" aria-label="Red protective shield with a raised stop hand"/>
    <line class="step-divider" x1="612" y1="640" x2="612" y2="718"/>
    <text class="step-text" x="634" y="644">Customized</text>
    <text class="step-text" x="634" y="675">continuous</text>
    <text class="step-text" x="634" y="706">protection</text>
  </g>

  <!-- maintain step -->
  <g class="step step-maintain">
    <rect x="275" y="334" width="180" height="104" rx="6" fill="url(#device-fill)" role="img" aria-label="Laptop and phone showing the facility monitoring app dashboard"/>
    <text class="step-text" x="305" y="477">Real-Time</text>
    <text class="step-text" x="305" y="508">Monitoring</text>
  </g>
</svg>
</body>
</html>
```